Bellcrest HVAC Business Card design

Looking for a modern professional two sided design. Showing contact info and services provided. Possibly on a silk card stock.
Using blues or greens or greys and maybe metallic. One color or a mixture of these.
Dorian Vance
dvance@bellcresthvac-example.net
555-318-4702
Air Conditioning
Heating
Heat Pumps / Gas / Oil
Ductless mini splits
Controls
VFD's
Pumps
Gas Fitting/Piping
Service and New install
Residential / Commercial
Industry/Entity Type
Mechanical HVAC
Contact Information for Business Card
Logo, contact info and provided services

```html
<!DOCTYPE html>
<html lang="en">
<head>
<meta charset="utf-8">
<title>Bellcrest HVAC Business Card</title>
<link rel="stylesheet" href="https://fonts.googleapis.com/css2?family=Montserrat:wght@400;500;600;800&display=swap">
<style>
  :root {
    --page-bg: #c9c9c9;
    --card-bg: #323232;
    --card-edge: #1b7fd1;
    --accent: #1b86dc;
    --text-light: #f1f1f1;
    --text-muted: #5b5b5b;
    --bullet: #4a4a4a;
  }
  * { box-sizing: border-box; margin: 0; padding: 0; }
  html, body { width: 1200px; height: 815px; overflow: hidden; }
  body {
    background: var(--page-bg);
    font-family: "Montserrat", sans-serif;
    color: var(--text-light);
    display: flex;
    align-items: center;
    justify-content: center;
    gap: 40px;
  }
  .card {
    position: relative;
    width: 560px;
    height: 320px;
    background: var(--card-bg);
    border-radius: 18px;
    border-bottom: 5px solid var(--card-edge);
    box-shadow: 0 10px 24px rgba(0,0,0,.3);
    overflow: hidden;
  }

  /* front */
  .brand-mark {
    position: absolute;
    left: 34px; top: 34px;
    display: flex; align-items: center; gap: 10px;
    font-weight: 600; font-size: 19px; color: var(--text-muted);
  }
  .brand-mark .dot {
    width: 22px; height: 22px; border-radius: 50%;
    background: var(--text-muted);
  }
  .identity { position: absolute; left: 34px; top: 118px; }
  .identity::before {
    content: ""; position: absolute; left: -34px; top: 4px;
    width: 22px; height: 46px; background: var(--accent);
  }
  .name { font-weight: 800; font-size: 30px; color: var(--accent); letter-spacing: .5px; line-height: 1; }
  .role { font-weight: 500; font-size: 14px; letter-spacing: 1px; margin-top: 6px; }
  .rule {
    position: absolute; left: 34px; right: 34px; top: 192px;
    height: 1px; background: var(--accent);
  }
  .contacts { position: absolute; left: 34px; top: 210px; list-style: none; }
  .contacts li {
    display: flex; align-items: center; gap: 9px;
    font-size: 12.5px; font-weight: 500; line-height: 25px;
  }
  .contacts svg { width: 13px; height: 13px; fill: var(--accent); flex: none; }
  .address {
    position: absolute; left: 330px; top: 212px;
    padding-left: 18px; border-left: 1px solid var(--accent);
    font-size: 12.5px; font-weight: 500; line-height: 24px; font-style: normal;
  }

  /* back */
  .back-brand {
    position: absolute; left: 0; right: 0; top: 78px;
    display: flex; align-items: center; justify-content: center; gap: 14px;
    font-weight: 600; font-size: 34px; color: var(--text-muted);
  }
  .back-brand .dot {
    width: 34px; height: 34px; border-radius: 50%; background: var(--text-muted);
  }
  .services {
    position: absolute; left: 30px; right: 30px; top: 196px;
    display: flex; flex-wrap: wrap; justify-content: center;
    column-gap: 16px; row-gap: 10px; list-style: none;
  }
  .services li {
    display: flex; align-items: center; gap: 7px;
    font-size: 13.5px; font-weight: 500;
  }
  .services li::before {
    content: ""; width: 11px; height: 11px; border-radius: 50%;
    background: var(--bullet); border: 1px solid #5e5e5e;
  }
  .services .break { flex-basis: 100%; height: 0; gap: 0; }
  .services .break::before { display: none; }
</style>
</head>
<body>
  <section class="card card-front" aria-label="Business card front">
    <div class="brand-mark"><span class="dot"></span>Bellcrest HVAC</div>
    <div class="identity">
      <h1 class="name">DORIAN VANCE</h1>
      <p class="role">MANAGER</p>
    </div>
    <div class="rule"></div>
    <ul class="contacts">
      <li><svg viewBox="0 0 24 24"><path d="M6.6 10.8a15.1 15.1 0 0 0 6.6 6.6l2.2-2.2a1 1 0 0 1 1-.25 11.4 11.4 0 0 0 3.6.57 1 1 0 0 1 1 1V20a1 1 0 0 1-1 1A17 17 0 0 1 3 4a1 1 0 0 1 1-1h3.5a1 1 0 0 1 1 1c0 1.25.2 2.45.57 3.57a1 1 0 0 1-.25 1z"/></svg>555-318-4702</li>
      <li><svg viewBox="0 0 24 24"><path d="M2 5h20v14H2zm2 2v.5l8 5 8-5V7l-8 5z"/></svg>dvance@bellcresthvac-example.net</li>
      <li><svg viewBox="0 0 24 24"><circle cx="12" cy="12" r="10"/></svg>www.bellcresthvac-example.net</li>
    </ul>
    <address class="address">
      482 North Ridge Road<br>
      STE 210<br>
      Your Country, MN 55012
    </address>
  </section>

  <section class="card card-back" aria-label="Business card back">
    <div class="back-brand"><span class="dot"></span>Bellcrest HVAC</div>
    <ul class="services">
      <li>Air Conditioning</li>
      <li>Heating</li>
      <li>Heat Pumps / Gas / Oil</li>
      <li class="break"></li>
      <li>Ductless mini splits</li>
      <li>Controls</li>
      <li>VFD's</li>
      <li>Pumps</li>
      <li class="break"></li>
      <li>Gas Fitting/Piping</li>
      <li>Service and New install</li>
      <li>Residential / Commercial</li>
    </ul>
  </section>
</body>
</html>
```